Kestrel Mobile App Design Concept

Design concept, including wireframe and design comps for a basketball themed Kestrel Mobile app.
Need example of a panorama page with 3 or 4 panels to include game schedule, news and a menu.
Example of a detail page showing game info or player info.
Note this quote is for a design concept.The chosen designer will be asked to work with our development team to build the full app. Familiarity with Balsamiq an advantage
Reason: Designs still in process from interested parties.
- 1. Must follow Kestrel Mobile guide lines
2. Must not look like an zelpad app
3. Dark theme and background

```html
<!DOCTYPE html>
<html lang="en">
<head>
<meta charset="utf-8">
<title>Kestrel Mobile – Basketball App Concept</title>
<link rel="stylesheet" href="https://fonts.googleapis.com/css2?family=Open+Sans:wght@400;600;700&display=swap">
<style>
  :root {
    --stage: #141414;
    --stage-edge: #0b0b0b;
    --screen: #101010;
    --bar: #1c1c1c;
    --orange: #e2680f;
    --orange-hot: #f07a14;
    --crimson: #7c1200;
    --accent-text: #d65a0c;
    --white: #ffffff;
    --muted: #9a9a9a;
    --chip: #4e4e4e;
  }
  * { box-sizing: border-box; margin: 0; padding: 0; }
  html, body { width: 1200px; height: 807px; overflow: hidden; }
  body {
    position: relative;
    background: radial-gradient(ellipse at 50% 40%, var(--stage) 0%, var(--stage-edge) 100%);
    font-family: "Open Sans", Arial, sans-serif;
    color: var(--white);
  }
  .abs { position: absolute; }
  .tile-fill { background: linear-gradient(to bottom, var(--crimson) 0%, #b63a06 45%, var(--orange) 100%); }

  /* Panorama page */
  .panorama { left: 507px; top: 138px; width: 548px; height: 487px; overflow: hidden; }
  .panorama__scene {
    position: absolute; inset: 0;
    background: linear-gradient(to bottom, #262626 0%, #2c2c2c 45%, #3a3128 70%, #5a4330 100%);
  }
  .panorama__topbar { position: absolute; left: 0; top: 0; width: 100%; height: 24px; background: var(--bar); }
  .panorama__title { left: 807px; top: 240px; font-size: 36px; font-weight: 600; color: var(--accent-text); line-height: 1; }

  .tile { position: absolute; width: 105px; height: 115px; }
  .tile__label { position: absolute; left: 6px; top: 5px; font-size: 12px; line-height: 1.1; }
  .tile__label--big { font-size: 18px; font-weight: 600; }
  .tile__label small { display: block; font-size: 11px; font-weight: 400; }
  .tile__photo { position: absolute; left: 0; bottom: 0; width: 100%; height: 58px; background: linear-gradient(135deg, #2a3150, #8a2a2a 60%, #3a3a44); }

  .profile__photo { left: 807px; top: 306px; width: 105px; height: 110px; background: linear-gradient(to bottom, #6d6d70, #3b3b3f 60%, #9a2a2e); }
  .profile__name { left: 918px; top: 303px; font-size: 19px; font-weight: 600; line-height: 1.1; }
  .profile__surname { left: 919px; top: 324px; font-size: 11px; }
  .profile__followers { left: 920px; top: 347px; font-size: 7.5px; color: var(--muted); }

  .stat { left: 807px; width: 220px; }
  .stat__label { position: absolute; left: 6px; bottom: 5px; font-size: 11px; }
  .stat__count { position: absolute; right: 10px; bottom: 2px; font-size: 32px; line-height: 1; }
  .stat__avatar { position: absolute; top: 0; width: 33px; height: 36px; background: linear-gradient(to bottom, #b9a89a, #5e4c42); }

  /* Phone screen */
  .screen { left: 187px; top: 140px; width: 284px; height: 485px; background: var(--screen); overflow: hidden; }
  .status { position: absolute; left: 0; top: 0; width: 100%; height: 14px; background: #000; }
  .status__time { position: absolute; right: 24px; top: 2px; font-size: 7px; color: var(--orange); }
  .status__signal { position: absolute; left: 14px; top: 4px; width: 8px; height: 6px; background: var(--orange); }
  .status__battery { position: absolute; left: 206px; top: 4px; width: 12px; height: 6px; border: 1px solid var(--orange); }
  .user-bar { position: absolute; left: 0; top: 22px; width: 100%; height: 40px; background: linear-gradient(to right, #1a1a1a, #000); }
  .user-bar__photo { position: absolute; left: 0; top: 0; width: 53px; height: 40px; background: linear-gradient(to bottom, #6b6b6b, #3a3a3a 60%, #8a2428); }
  .user-bar__name { position: absolute; left: 61px; top: 15px; font-size: 8.5px; font-weight: 700; }
  .user-bar__points { position: absolute; left: 185px; top: 13px; font-size: 10.5px; font-weight: 700; }
  .user-bar__alerts { position: absolute; right: 0; top: 0; width: 42px; height: 40px; background: #2a2a2a; }
  .user-bar__badge { position: absolute; left: 11px; top: 10px; width: 18px; height: 18px; background: #e5421a; font-size: 9px; font-weight: 700; text-align: center; line-height: 18px; }

  .menu { position: absolute; left: 12px; top: 112px; width: 230px; list-style: none; }
  .menu__item { position: relative; font-size: 26px; line-height: 37px; height: 37px; }
  .menu__arrow { position: absolute; right: 0; top: 6px; }

  .news__heading { position: absolute; left: 14px; top: 320px; font-size: 16.5px; }
  .news__filter { position: absolute; left: 14px; top: 348px; width: 223px; height: 16px; background: var(--chip); font-size: 11.5px; line-height: 16px; padding-left: 5px; }
  .news__photo { position: absolute; left: 15px; top: 370px; width: 85px; height: 78px; background: linear-gradient(to bottom, #c9c9c9, #7a3a2a 60%, #b02020); }
  .news__title { position: absolute; left: 111px; top: 370px; font-size: 12.5px; line-height: 1.05; }
  .news__body { position: absolute; left: 111px; top: 400px; width: 130px; font-size: 6.8px; line-height: 1.45; color: #ddd; }

  .appbar { position: absolute; left: 0; bottom: 0; width: 100%; height: 37px; background: linear-gradient(to bottom, #a42a04, var(--orange)); }
  .appbar__btn { position: absolute; top: 8px; }
  .appbar__more { position: absolute; right: 12px; top: 2px; font-size: 10px; letter-spacing: 1px; }
</style>
</head>
<body>

  <!-- Panorama page -->
  <section class="panorama abs">
    <div class="panorama__scene" role="img" aria-label="Dim indoor basketball court with hoop and wooden floor"></div>
    <div class="panorama__topbar"></div>
  </section>

  <h1 class="panorama__title abs">you</h1>

  <div class="tile tile-fill" style="left:441px;top:306px"><span class="tile__label">Preferences</span></div>
  <div class="tile tile-fill" style="left:551px;top:306px">
    <span class="tile__label tile__label--big">PBL<small>news</small></span>
    <div class="tile__photo" role="img" aria-label="Two basketball players in game jerseys"></div>
  </div>
  <div class="tile tile-fill" style="left:663px;top:306px"><span class="tile__label">Worldwide<br>Game Shedules</span></div>
  <div class="tile tile-fill" style="left:441px;top:430px">
    <span class="tile__label">Dunks</span>
    <div class="tile__photo" role="img" aria-label="Player dunking at the hoop"></div>
  </div>
  <div class="tile tile-fill" style="left:551px;top:430px"><span class="tile__label" style="font-size:14px">Teams</span></div>

  <div class="profile__photo abs" role="img" aria-label="Profile photo of the user"></div>
  <div class="profile__name abs">Marcus</div>
  <div class="profile__surname abs">Tellaro</div>
  <div class="profile__followers abs">Followers : 35</div>

  <div class="stat tile-fill abs" style="top:432px;height:64px">
    <div class="stat__avatar" style="left:1px" role="img" aria-label="Visitor avatar"></div>
    <div class="stat__avatar" style="left:69px" role="img" aria-label="Visitor avatar"></div>
    <div class="stat__avatar" style="left:102px" role="img" aria-label="Visitor avatar"></div>
    <span class="stat__label">Who viewed your profile</span>
    <span class="stat__count">3</span>
  </div>
  <div class="stat tile-fill abs" style="top:508px;height:67px">
    <span class="stat__label">People you may know</span>
    <span class="stat__count">0</span>
  </div>

  <!-- Phone screen -->
  <section class="screen abs">
    <div class="status">
      <span class="status__signal"></span>
      <span class="status__battery"></span>
      <span class="status__time">12:22</span>
    </div>

    <div class="user-bar">
      <div class="user-bar__photo" role="img" aria-label="User avatar"></div>
      <span class="user-bar__name">MARCUS T.</span>
      <span class="user-bar__points">24685 ›</span>
      <div class="user-bar__alerts"><div class="user-bar__badge">3</div></div>
    </div>

    <ul class="menu">
      <li class="menu__item">Preferences<svg class="menu__arrow" width="26" height="26" viewBox="0 0 26 26"><circle cx="13" cy="13" r="11.5" fill="none" stroke="#fff" stroke-width="2"/><path d="M7 13h11M13 8l5 5-5 5" fill="none" stroke="#fff" stroke-width="2.2"/></svg></li>
      <li class="menu__item">Sync<svg class="menu__arrow" width="26" height="26" viewBox="0 0 26 26"><circle cx="13" cy="13" r="11.5" fill="none" stroke="#fff" stroke-width="2"/><path d="M7 13h11M13 8l5 5-5 5" fill="none" stroke="#fff" stroke-width="2.2"/></svg></li>
      <li class="menu__item">Teams<svg class="menu__arrow" width="26" height="26" viewBox="0 0 26 26"><circle cx="13" cy="13" r="11.5" fill="none" stroke="#fff" stroke-width="2"/><path d="M7 13h11M13 8l5 5-5 5" fill="none" stroke="#fff" stroke-width="2.2"/></svg></li>
      <li class="menu__item">Help<svg class="menu__arrow" width="26" height="26" viewBox="0 0 26 26"><circle cx="13" cy="13" r="11.5" fill="none" stroke="#fff" stroke-width="2"/><path d="M7 13h11M13 8l5 5-5 5" fill="none" stroke="#fff" stroke-width="2.2"/></svg></li>
      <li class="menu__item">Gallery<svg class="menu__arrow" width="26" height="26" viewBox="0 0 26 26"><circle cx="13" cy="13" r="11.5" fill="none" stroke="#fff" stroke-width="2"/><path d="M7 13h11M13 8l5 5-5 5" fill="none" stroke="#fff" stroke-width="2.2"/></svg></li>
    </ul>

    <h2 class="news__heading">Latest news</h2>
    <div class="news__filter">world</div>
    <div class="news__photo" role="img" aria-label="Player in red jersey mid-dunk"></div>
    <h3 class="news__title">Darren Holt<br>can still dunk at age 50</h3>
    <p class="news__body">Sure, it's great to see the Lakeview Hawks legend/Hall of Famer/greatest basketball player of all time take flight once more, but if D.H. wants to impress us, he's going to need to step his game up a level.</p>

    <div class="appbar">
      <svg class="appbar__btn" style="left:102px" width="24" height="24" viewBox="0 0 24 24"><circle cx="12" cy="12" r="11" fill="none" stroke="#fff" stroke-width="1.5"/><rect x="7" y="7" width="10" height="8" fill="#fff"/><path d="M9 15v3l3-3" fill="#fff"/></svg>
      <svg class="appbar__btn" style="left:153px" width="24" height="24" viewBox="0 0 24 24"><circle cx="12" cy="12" r="11" fill="none" stroke="#fff" stroke-width="1.5"/><circle cx="13" cy="10.5" r="3.5" fill="none" stroke="#fff" stroke-width="1.5"/><path d="M10.5 13l-3.5 3.5" stroke="#fff" stroke-width="1.8"/></svg>
      <span class="appbar__more">•••</span>
    </div>
  </section>

</body>
</html>
```